WordPress Site That Reviews Footwear

We need a wordpress web design for an affiliate site called TreadNest. We review and do roundups on footwear products. The final design should be clean and mobile friendly. The site should be built with Gutenberg page builder. We like the design of https://dermalquill.com/.
Updates

Need extra days to review

Target Market(s)

USA

Industry/Entity Type

Footwear

Logo Text

TreadNest

Number of Pages Required

4 page

Font styles to use
Serif
Sans Serif

Requirements
Must have
• Wordpress site
Blog post
Page
Categories
Homepage

```html
<!DOCTYPE html>
<html lang="en">
<head>
<meta charset="utf-8">
<title>5 Easy Shoe Care Tips For Happy Feet – TreadNest</title>
<link href="https://fonts.googleapis.com/css2?family=Playfair+Display:wght@400;700&family=Poppins:wght@300;400;500;600;700&display=swap" rel="stylesheet">
<style>
:root{
  --ink:#111;
  --text:#333;
  --muted:#555;
  --accent:#f2bb05;
  --band:#f4f4f4;
  --field:#e8e8e8;
  --rule:#dcdcdc;
  --serif:'Playfair Display',serif;
  --sans:'Poppins',sans-serif;
}
*{margin:0;padding:0;box-sizing:border-box}
html,body{width:1200px;height:2279px;overflow:hidden;background:#fff;font-family:var(--sans);color:var(--text)}
.abs{position:absolute}
a{color:inherit;text-decoration:none}

.site-header{position:absolute;left:0;top:0;width:1200px;height:77px}
.nav{position:absolute;top:34px;display:flex;gap:26px;font-size:13.5px;color:var(--ink);letter-spacing:.2px}
.nav-left{left:88px}
.nav-right{left:851px}
.brand{position:absolute;left:0;width:1200px;top:18px;text-align:center;font-family:var(--serif);font-size:35px;font-weight:700;color:var(--ink)}
.header-icons{position:absolute;left:1022px;top:33px;display:flex;gap:12px;align-items:center}
.cart-count{position:absolute;left:1097px;top:30px;width:14px;height:14px;border-radius:50%;background:var(--accent);font-size:9px;text-align:center;line-height:14px;color:var(--ink)}

.breadcrumb{position:absolute;top:77px;left:0;width:1200px;height:43px;background:var(--band);padding:12px 88px;font-size:14.5px;color:var(--muted)}
.breadcrumb strong{font-weight:500;color:#333}

.hero{left:87px;top:165px;width:718px;height:361px;border-radius:6px;background:linear-gradient(160deg,#cfcfcf 0%,#a9a9a9 45%,#8a8a8a 100%)}

.article{left:88px;top:572px;width:700px}
.article h1{font-family:var(--serif);font-size:39px;font-weight:700;color:var(--ink);line-height:50px}
.article .date{font-size:17px;color:#444;margin-left:2px;margin-bottom:8px}
.article p{font-size:16px;line-height:26.7px;color:#444;margin-left:2px}
.article h3{font-size:18px;font-weight:600;color:var(--ink);margin:14px 0 8px}
.collection{font-size:15.5px;line-height:28.5px;color:#444;margin-bottom:10px}
.quote{font-size:16px;line-height:26.7px;color:#444;margin-left:2px}
.cite{font-size:18px;font-weight:500;color:var(--accent);margin:4px 0 0 3px}
.cite span{margin-right:22px}
.share{display:inline-block;margin:36px 0 0 3px;font-size:19px;font-weight:500;color:#222;border-bottom:1px solid #222;line-height:24px}

.comment-title{left:88px;top:1362px;width:717px;border-bottom:2px solid #e6e6e6;padding-bottom:6px;font-family:var(--serif);font-size:40px;font-weight:700;color:var(--ink)}
.field{background:var(--field);font-size:19px;font-weight:500;color:#333;padding:16px 21px}
.btn-submit{left:86px;top:1741px;width:242px;height:52px;border-radius:6px;background:var(--accent);font-size:19px;font-weight:700;color:var(--ink);text-align:center;line-height:52px;letter-spacing:.3px}

.sidebar{left:849px;width:262px}
.search-box{top:164px;height:75px;background:var(--accent);padding:23px 21px}
.search-box .input{display:flex;height:32px;background:#fff;border-radius:3px;overflow:hidden}
.search-box .input span{flex:1;font-size:12.5px;color:#444;padding:8px 16px}
.search-box .input i{width:33px;background:var(--ink);display:flex;align-items:center;justify-content:center}
.side-title{font-family:var(--serif);font-size:21px;font-weight:700;color:var(--ink)}
.post-row{display:flex;align-items:center;gap:18px;height:85px;border-bottom:1px solid var(--rule)}
.post-thumb{width:69px;height:69px;background:linear-gradient(135deg,#d8d2cc,#6d5a4b)}
.post-row b{display:block;font-size:14px;font-weight:700;color:var(--ink)}
.post-row small{font-size:12px;color:#444}
.socials{display:flex;gap:7px}
.socials span{width:36px;height:36px;border-radius:50%}
.newsletter{top:700px;height:223px;background:#efefef;text-align:center;padding-top:44px}
.newsletter h2{font-family:var(--serif);font-size:32px;font-weight:700;color:var(--ink);line-height:38px}
.newsletter p{font-size:12px;line-height:18px;color:#555;margin:6px 18px 12px}
.newsletter .row{display:flex;margin:0 15px 0 19px;height:40px}
.newsletter .row span{flex:1;background:#fff;text-align:left;font-size:12.5px;color:#666;padding:12px 15px}
.newsletter .row i{width:47px;background:var(--accent);display:flex;align-items:center;justify-content:center}
.ad{top:934px;height:339px;background:linear-gradient(115deg,#f4c7cd 0%,#d9a9b2 48%,#b8b8b8 52%,#a3a3a3 100%);display:flex;flex-direction:column;align-items:center;justify-content:center;color:#fff}
.ad b{font-size:48px;font-weight:700;line-height:46px}
.ad span{font-size:25px;font-weight:600}

.footer{left:0;top:1883px;width:1200px;height:396px;background:var(--band)}
.fcol{position:absolute;top:97px}
.fcol h4{font-family:var(--serif);font-size:19px;font-weight:700;color:var(--ink);letter-spacing:.3px;margin-bottom:6px}
.fcol li{list-style:none;font-size:13.5px;line-height:22.3px;color:#444;margin-left:1px}
.femail{position:absolute;left:824px;top:120px;width:287px;height:32px;border-bottom:3px solid var(--accent);font-size:23px;font-weight:600;color:#b5b5b5;padding-left:5px}
.femail svg{position:absolute;right:8px;top:4px}
.frule{position:absolute;left:88px;top:341px;width:1023px;border-top:1px solid var(--rule)}
.copy{position:absolute;left:88px;top:361px;font-size:14px;color:#222}
.pay{position:absolute;top:358px;display:flex;gap:10px;left:976px}
.pay span{width:43px;height:27px;border-radius:5px}
.to-top{position:absolute;left:1140px;top:322px;width:31px;height:31px;border-radius:50%;background:var(--accent);display:flex;align-items:center;justify-content:center}
</style>
</head>
<body>

<header class="site-header">
  <nav class="nav nav-left"><a>WOMENS</a><a>MENS</a><a>KIDS</a><a>SALE</a></nav>
  <div class="brand">TreadNest</div>
  <nav class="nav nav-right"><a>ABOUT</a><a>CONTACT</a></nav>
  <div class="header-icons">
    <svg width="18" height="18" viewBox="0 0 18 18" fill="none" stroke="#111" stroke-width="2"><circle cx="7.5" cy="7.5" r="6"/><path d="M12 12l5 5"/></svg>
    <svg width="18" height="18" viewBox="0 0 18 18" fill="none" stroke="#111" stroke-width="1.6"><circle cx="9" cy="6" r="4"/><path d="M2 17c0-4 3-6 7-6s7 2 7 6"/></svg>
    <svg width="18" height="18" viewBox="0 0 18 18" fill="none" stroke="#111" stroke-width="1.6"><path d="M3 6h12l-1 11H4z"/><path d="M6 6V4a3 3 0 016 0v2"/></svg>
  </div>
  <div class="cart-count">0</div>
</header>

<div class="breadcrumb">Home &gt; Blog Post &gt; <strong>5 Easy Shoe Care Tips For Happy Feet</strong></div>

<div class="abs hero" role="img" aria-label="Photo of white leather sneakers on a speckled stone floor beside a wall"></div>

<article class="abs article">
  <h1>5 Easy Shoe Care Tips For Happy Feet</h1>
  <div class="date">Date: Aug-10-2020</div>
  <p>Lorem Ipsum is simply dummy text of the printing and typesetting industry. Lorem Ipsum has been the industry's standard dummy text ever since the 1500s, when an unknown printer took a galley of type and scrambled it to make a type specimen book. It has survived not only five centuries, but also the leap into electronic typesetting, remaining essentially un-changed. It was popularised in the 1960s with the release .</p>
  <h3>Shop Our Collection:</h3>
  <div class="collection">
    Men’s - Strideline Glide 13 Charcoal/Black available in medium width and wide width<br>
    Women’s - Strideline Glide 13 Coral available in medium width<br>
    Women’s - Strideline Glide 13 Blush/Dusk available in medium width and wide width
  </div>
  <p>Lorem Ipsum is simply dummy text of the printing and typesetting industry. Lorem Ipsum has been the industry's standard dummy text ever since the 1500s, when an unknown printer took a galley of type and scrambled it to make a type specimen book. It has survived not only five centuries, but also the leap into electronic typesetting, remaining essentially un-changed. It was popularised in the 1960s .</p>
  <h3 style="margin-top:16px">Testimonials</h3>
  <p class="quote">”Lorem Ipsum is simply dummy text of the printing and typesetting industry. Lorem Ipsum has been the industry's standard dummy text ever since the 1500s, when an un-known printer took a galley of type and scrambled it to make a type ..</p>
  <div class="cite"><span>-</span>Mara Ellison, Strideline Athlete</div>
  <div class="share">Share this blog to your friends</div>
</article>

<h2 class="abs comment-title">Post Comment</h2>
<div class="abs field" style="left:88px;top:1468px;width:339px;height:52px">Name</div>
<div class="abs field" style="left:434px;top:1468px;width:339px;height:52px">Email</div>
<div class="abs field" style="left:88px;top:1528px;width:685px;height:202px">Comment</div>
<div class="abs btn-submit">SUBMIT COMMENT</div>

<aside>
  <div class="abs sidebar search-box"><div class="input"><span>Search here</span><i><svg width="11" height="11" viewBox="0 0 12 12" fill="none" stroke="#fff" stroke-width="1.5"><circle cx="5" cy="5" r="3.8"/><path d="M8 8l3 3"/></svg></i></div></div>
  <div class="abs sidebar" style="top:258px"><div class="side-title">Recent Posts</div></div>
  <div class="abs sidebar" style="top:291px;border-bottom:1px solid var(--rule);padding-bottom:14px">
    <div class="post-row"><div class="post-thumb" role="img" aria-label="Photo of assorted sports shoes"></div><div><b>Top 5 Best Cricket Shoes</b><small>June 14, 2021</small></div></div>
    <div class="post-row"><div class="post-thumb" role="img" aria-label="Photo of leather dress shoes"></div><div><b>Shoes a Fashion .</b><small>June 14, 2021</small></div></div>
    <div class="post-row" style="border:0"><div class="post-thumb" role="img" aria-label="Photo of brown leather shoes"></div><div><b>Top 5 Best Cricket Shoes</b><small>June 14, 2021</small></div></div>
  </div>
  <div class="abs sidebar" style="top:590px"><div class="side-title">Follow Us</div></div>
  <div class="abs sidebar socials" style="top:628px"><span style="background:#3b5a9a"></span><span style="background:#1da1f2"></span><span style="background:#dd4b39"></span><span style="background:#0e5a8a"></span></div>
  <div class="abs sidebar newsletter">
    <h2>Newsletter</h2>
    <p>Lorem ipsum dolor sit amet, consectetu er adipiscing elit aenean .</p>
    <div class="row"><span>Email address</span><i><svg width="14" height="14" viewBox="0 0 16 16"><path d="M1 7l14-6-5 14-2-6z" fill="#111"/></svg></i></div>
  </div>
  <div class="abs sidebar ad" role="img" aria-label="Advertisement space with photo of sandals and white sneakers"><b>250x250</b><span>ADVERTISMENT</span></div>
</aside>

<footer class="abs footer">
  <div class="fcol" style="left:88px"><h4>COMPANY INFO</h4><ul><li>About</li><li>Corporate video</li><li>Blog</li><li>Contact Us</li></ul></div>
  <div class="fcol" style="left:338px"><h4>WHAT'S IN STORE</h4><ul><li>New Arrivals</li><li>Men</li><li>Women</li><li>Kids</li><li>Accessories</li><li>Brands</li></ul></div>
  <div class="fcol" style="left:596px"><h4>HELP &amp; SUPPORT</h4><ul><li>Exchange &amp; Returns</li><li>Privacy Policy</li><li>FAQ</li></ul></div>
  <div class="femail">Enter your email<svg width="20" height="20" viewBox="0 0 16 16"><path d="M1 7l14-6-5 14-2-6z" fill="#111"/></svg></div>
  <div class="to-top"><svg width="10" height="8" viewBox="0 0 10 8" fill="none" stroke="#111" stroke-width="1.8"><path d="M1 6l4-4 4 4"/></svg></div>
  <div class="frule"></div>
  <div class="copy">©Copyright 2021 | All Rights Reserved</div>
  <div class="pay"><span style="background:#e9e9e9"></span><span style="background:#1a3a8f"></span><span style="background:#e9e9e9"></span></div>
</footer>

</body>
</html>
```